BrindleStaffing Business Card Design

We are a staffing company finding positions for dedicated nurses and physicians.

Target Market(s)

Business Professionals

Industry/Entity Type

Staffing

Contact Information for Business Card

Gregory Malden
Chairman
417 39th Crescent South
SAINT PETERSBURG FL 33719
813-555-0147 Mobile
813-555-0183 Fax
gmalden@brindlestaffing.example
www.brindlestaffing.example

Font styles to use
Sans Serif

Colors
fbee3e
f04a50
f37122

Requirements
Must have
• Logo Attached, see colors below. We'd like to see Yellow, Orange and Red.

```html
<!DOCTYPE html>
<html lang="en">
<head>
<meta charset="utf-8">
<title>BrindleStaffing Business Card</title>
<link rel="stylesheet" href="https://fonts.googleapis.com/css2?family=Roboto:wght@400;500;700&display=swap">
<style>
  :root {
    --page-bg: #e9e7e3;
    --card-white: #ffffff;
    --card-dark: #1b1d1e;
    --brand-yellow: #fbee3e;
    --brand-red: #f04a50;
    --brand-orange: #f37122;
    --body-grey: #4a4a4a;
    --rule-grey: #b9b9b9;
  }
  * { box-sizing: border-box; margin: 0; padding: 0; }
  html, body { width: 1200px; height: 1040px; overflow: hidden; }
  body {
    background: var(--page-bg);
    font-family: "Roboto", Arial, sans-serif;
    position: relative;
  }
  .card {
    position: absolute;
    left: 240px;
    width: 720px;
    height: 411px;
    border-radius: 30px;
    box-shadow: 0 10px 28px rgba(0,0,0,0.18);
  }
  .card-frame {
    position: absolute;
    inset: 22px;
    border: 1.5px solid var(--brand-orange);
    border-radius: 22px;
  }
  .card-front {
    top: 70px;
    background: var(--card-white);
  }
  .front-content {
    position: absolute;
    inset: 0;
    display: flex;
    flex-direction: column;
    align-items: center;
    justify-content: center;
    text-align: center;
  }
  .holder-name {
    color: var(--brand-orange);
    font-weight: 700;
    font-size: 40px;
    line-height: 1.1;
  }
  .holder-title {
    color: var(--brand-red);
    font-weight: 500;
    font-size: 19px;
    margin-top: 4px;
  }
  .divider {
    width: 38px;
    height: 2px;
    background: var(--rule-grey);
    margin: 18px 0 20px;
  }
  .contact-line {
    color: var(--body-grey);
    font-size: 16px;
    line-height: 1.55;
  }
  .card-back {
    top: 560px;
    background: var(--card-dark);
  }
  .brand {
    position: absolute;
    inset: 0;
    display: flex;
    align-items: center;
    justify-content: center;
    gap: 14px;
  }
  .brand-name {
    color: var(--brand-yellow);
    font-weight: 700;
    font-size: 62px;
    letter-spacing: -1px;
  }
  .brand-dot {
    width: 18px;
    height: 18px;
    border-radius: 50%;
    background: var(--brand-red);
  }
</style>
</head>
<body>
  <section class="card card-front">
    <div class="card-frame"></div>
    <div class="front-content">
      <h1 class="holder-name">Gregory Malden</h1>
      <p class="holder-title">Chairman</p>
      <div class="divider"></div>
      <p class="contact-line">417 39th Crescent South, SAINT PETERSBURG FL 33719</p>
      <p class="contact-line">C: 813-555-0147 F: 813-555-0183 E: gmalden@brindlestaffing.example</p>
      <p class="contact-line">www.brindlestaffing.example</p>
    </div>
  </section>

  <section class="card card-back">
    <div class="card-frame"></div>
    <div class="brand">
      <span class="brand-name">BrindleStaffing</span>
      <span class="brand-dot"></span>
    </div>
  </section>
</body>
</html>
```